card design for engineering consultancy

engineering drafting and project management company the provides drafting services for.
Electrical, Hydraulic, Mechanical, and Civil services
The company is called Q7R Services and logo is as attached
Information on card should be.
1. Logo
2.website : Q7RServices.example
3. email : info@Q7RServices.example
4. Phone: (+61) 400512836
5. Motto: Design - Document - Develop - Deliver

this card should be basically used for business identification only

Target Market(s)

electricians plumbers air conditioning installers and civil contractors

Industry/Entity Type

engineering, drafting, electrical, plumbing, airconditioning, civil

Contact Information for Business Card

1. Logo 2.website : Q7RServices.example 3. email : info@Q7RServices.example 4. Phone: (+61) 400512836 5. Motto: Design - Document - Develop - Deliver

Font styles to use
Serif

Requirements
Must have
• logo
Nice to have
• something inovative and different that makes it stand out from being just another business card

```html
<!DOCTYPE html>
<html lang="en">
<head>
<meta charset="utf-8">
<title>Q7R Services – Business Card</title>
<link rel="stylesheet" href="https://fonts.googleapis.com/css2?family=Roboto:wght@400;500;700&display=swap">
<style>
  :root {
    --page-bg: #fafafa;
    --card-dark-1: #2b2e32;
    --card-dark-2: #0c0c0d;
    --logo-grey: #d6d6d6;
    --brand-red: #d11f26;
    --band-grey: #43474c;
    --text-light: #f2f2f2;
  }
  * { margin: 0; padding: 0; box-sizing: border-box; }
  html, body {
    width: 800px;
    height: 1200px;
    overflow: hidden;
    background: var(--page-bg);
    font-family: "Roboto", Arial, sans-serif;
  }
  .sheet {
    position: relative;
    width: 800px;
    height: 1200px;
  }
  .card {
    position: absolute;
    left: 80px;
    width: 640px;
    height: 365px;
    background: linear-gradient(160deg, var(--card-dark-1) 0%, #17181a 55%, var(--card-dark-2) 100%);
    box-shadow: 0 3px 10px rgba(0,0,0,0.25);
    overflow: hidden;
  }
  .card--front { top: 205px; }
  .card--back { top: 625px; }

  .brand-name {
    position: absolute;
    left: 0;
    right: 0;
    text-align: center;
    color: var(--logo-grey);
    font-weight: 700;
    text-transform: uppercase;
    letter-spacing: 0.12em;
    white-space: nowrap;
  }
  .card--front .brand-name { top: 72px; font-size: 40px; }
  .card--back .brand-name { top: 126px; font-size: 50px; }

  .contact-icon {
    position: absolute;
    top: 216px;
    width: 32px;
    height: 36px;
  }
  .contact-icon--phone { left: 89px; }
  .contact-icon--email { left: 304px; }
  .contact-icon--web { left: 517px; }

  .contact-band {
    position: absolute;
    top: 253px;
    left: 0;
    width: 640px;
    height: 30px;
  }
  .contact-item {
    position: absolute;
    top: 0;
    height: 30px;
    background: var(--band-grey);
    color: var(--text-light);
    font-size: 17px;
    line-height: 30px;
    text-align: center;
    white-space: nowrap;
  }
  .contact-item--phone { left: 0; width: 196px; }
  .contact-item--email { left: 201px; width: 238px; }
  .contact-item--web { left: 444px; width: 196px; }

  .motto-band {
    position: absolute;
    left: 0;
    top: 283px;
    width: 640px;
    height: 82px;
    background: var(--brand-red);
    color: var(--text-light);
    font-size: 21px;
    font-weight: 500;
    line-height: 82px;
    text-align: center;
  }

  .back-website {
    position: absolute;
    left: 0;
    right: 0;
    top: 308px;
    text-align: center;
    color: var(--brand-red);
    font-size: 17px;
    font-weight: 700;
  }
</style>
</head>
<body>
<main class="sheet">

  <section class="card card--front" aria-label="Business card front">
    <p class="brand-name">Q7R Services</p>

    <svg class="contact-icon contact-icon--phone" viewBox="0 0 32 36" aria-hidden="true">
      <rect x="0" y="0" width="32" height="30" rx="6" fill="var(--brand-red)"/>
      <path d="M12 31 L16 36 L20 31 Z" fill="var(--brand-red)"/>
      <path d="M11 7 c-2 1 -3 3 -2 6 c1 4 5 9 9 10 c2 1 4 0 5 -2 l-3 -3 c-1 1 -2 1 -3 0 c-2 -1 -3 -3 -4 -5 c0 -1 0 -2 1 -2 z" fill="#fff"/>
    </svg>
    <svg class="contact-icon contact-icon--email" viewBox="0 0 32 36" aria-hidden="true">
      <rect x="0" y="0" width="32" height="30" rx="6" fill="var(--brand-red)"/>
      <path d="M12 31 L16 36 L20 31 Z" fill="var(--brand-red)"/>
      <rect x="6" y="8" width="20" height="14" fill="#fff"/>
      <path d="M6 8 L16 16 L26 8" fill="none" stroke="var(--brand-red)" stroke-width="2"/>
    </svg>
    <svg class="contact-icon contact-icon--web" viewBox="0 0 32 36" aria-hidden="true">
      <rect x="0" y="0" width="32" height="30" rx="6" fill="var(--brand-red)"/>
      <path d="M12 31 L16 36 L20 31 Z" fill="var(--brand-red)"/>
      <g fill="none" stroke="#fff" stroke-width="1.8">
        <circle cx="16" cy="15" r="9"/>
        <ellipse cx="16" cy="15" rx="4" ry="9"/>
        <line x1="7" y1="15" x2="25" y2="15"/>
        <line x1="9" y1="10" x2="23" y2="10"/>
        <line x1="9" y1="20" x2="23" y2="20"/>
      </g>
    </svg>

    <div class="contact-band">
      <p class="contact-item contact-item--phone">(+61) 400512836</p>
      <p class="contact-item contact-item--email">info@Q7RServices.example</p>
      <p class="contact-item contact-item--web">Q7RServices.example</p>
    </div>

    <p class="motto-band">Design - Document - Develop - Deliver</p>
  </section>

  <section class="card card--back" aria-label="Business card back">
    <p class="brand-name">Q7R Services</p>
    <p class="back-website">Q7RServices.example</p>
  </section>

</main>
</body>
</html>
```